LOMADRIS COFFEE CUPS

I WANT A DESIGN FOR TAKE AWAY COFFEE CUPS 12 oz. IN THE ATTACHED PROFILES YOU'LL FIND THE LOGO AND SOME DESIGNS I LIKE (WHICH IS FLOWER OR COFFEE QOUTES) THE COLORS ARE PREFERLY WHITE, PINK, PURPLE OR YOU CAN DO OTHER COLORS IF NICER.

```html
<!DOCTYPE html>
<html lang="en">
<head>
<meta charset="utf-8">
<title>Lomadris Coffee – 12 oz Take Away Cup</title>
<link rel="stylesheet" href="https://fonts.googleapis.com/css2?family=Oswald:wght@500&family=Special+Elite&display=swap">
<style>
  :root {
    --page: #ffffff;
    --frame: #4a4a4a;
    --cup-paper: #fffdf0;
    --cup-edge: #2f2f2f;
    --brand-purple: #a24fa6;
    --quote-pink: #e8489a;
    --wreath-green: #9bbf6a;
    --wreath-coral: #f08a5d;
    --wreath-rose: #f3a6c0;
  }
  html, body {
    margin: 0;
    padding: 0;
    width: 965px;
    height: 1200px;
    overflow: hidden;
    background: var(--page);
  }
  .artboard {
    position: relative;
    width: 965px;
    height: 1200px;
    box-sizing: border-box;
    border: 1px solid var(--frame);
    background: var(--page);
  }
  .cup-outline {
    position: absolute;
    inset: 0;
  }
  .brand {
    position: absolute;
    left: 282px;
    top: 160px;
    width: 380px;
    font-family: "Oswald", sans-serif;
    font-weight: 500;
    color: var(--brand-purple);
    text-align: right;
  }
  .brand-name {
    display: block;
    font-size: 104px;
    line-height: 1;
    text-align: center;
    letter-spacing: 1px;
  }
  .brand-descriptor {
    display: block;
    margin-top: 6px;
    font-size: 28px;
    line-height: 1;
    letter-spacing: 7px;
  }
  .floral-wreath {
    position: absolute;
    left: 221px;
    top: 437px;
    width: 500px;
    height: 500px;
  }
  .quote {
    position: absolute;
    left: 271px;
    top: 560px;
    width: 400px;
    margin: 0;
    font-family: "Special Elite", cursive;
    color: var(--quote-pink);
    text-align: center;
    font-size: 54px;
    line-height: 62px;
    letter-spacing: 2px;
  }
  .quote-heart {
    position: absolute;
    left: 416px;
    top: 742px;
    width: 108px;
    height: 98px;
  }
</style>
</head>
<body>
<main class="artboard">
  <svg class="cup-outline" width="965" height="1200" viewBox="0 0 965 1200" aria-hidden="true">
    <polygon points="117,111 825,111 706,1135 236,1135" fill="var(--cup-paper)" stroke="var(--cup-edge)" stroke-width="1.2"/>
  </svg>

  <div class="brand">
    <span class="brand-name">Lomadris</span>
    <span class="brand-descriptor">COFFEE</span>
  </div>

  <svg class="floral-wreath" viewBox="0 0 500 500" role="img" aria-label="Watercolour wreath of flowers, vines, butterflies and a small bird">
    <defs>
      <linearGradient id="wreathTone" x1="0" y1="0" x2="1" y2="1">
        <stop offset="0" stop-color="var(--wreath-coral)"/>
        <stop offset="0.5" stop-color="var(--wreath-green)"/>
        <stop offset="1" stop-color="var(--wreath-rose)"/>
      </linearGradient>
    </defs>
    <circle cx="250" cy="250" r="225" fill="none" stroke="url(#wreathTone)" stroke-width="34" opacity="0.45"/>
  </svg>

  <p class="quote">A<br>LIQUID<br>OF LOVE</p>

  <svg class="quote-heart" viewBox="0 0 108 98" role="img" aria-label="Hand-scribbled pink heart">
    <path d="M54 96 C20 70 2 52 2 30 C2 12 16 2 30 2 C42 2 50 10 54 18 C58 10 66 2 78 2 C92 2 106 12 106 30 C106 52 88 70 54 96 Z" fill="var(--quote-pink)" opacity="0.85"/>
  </svg>
</main>
</body>
</html>
```